Invite to The Halvorsen Project

You’re Cordially Invited
To a Sunset Celebration Honoring the Launch of The Halvorsen

Date: Thursday, May 15
Time: 5:30 PM – 7:30 PM
Location: The Halvorsen, 214 Quillfield Street, East Boston

Please join us for an elegant evening of connection and celebration as we unveil The Halvorsen Project.
Enjoy private tours of Units 3 and 4, along with our breathtaking roof deck offering sweeping views of East Boston at sunset.

Sip curated selections of beer and wine and savor light seasonal bites as you mingle with colleagues and guests.

Feel free to bring clients, friends, or family — all are welcome!

Kindly RSVP to:
Marisol Penwarden, Larchmont Realty
📧 Marisol@larchmontexample.com

Please include logo, classic design, and attachments. Colors navy, gold, white

```html
<!DOCTYPE html>
<html lang="en">
<head>
<meta charset="utf-8">
<title>Invite to The Halvorsen Project</title>
<link rel="stylesheet" href="https://fonts.googleapis.com/css2?family=Lora:ital,wght@0,400;1,400&family=Fira+Sans:wght@300;400&family=Libre+Baskerville:wght@700&display=swap">
<style>
  :root {
    --navy: #253553;
    --gold: #e8b04a;
    --gold-soft: rgba(232, 176, 74, 0.22);
    --ink: #eceae4;
    --white: #ffffff;
    --sky: #5b8fd4;
    --facade: #3b3a38;
    --cladding: #b07a4a;
    --street: #8d8c8a;
  }
  * { margin: 0; padding: 0; box-sizing: border-box; }
  html, body { width: 1200px; height: 851px; overflow: hidden; background: var(--navy); }
  .invite {
    position: relative;
    width: 1200px;
    height: 851px;
    display: flex;
  }
  .building-photo {
    width: 511px;
    height: 851px;
    background: linear-gradient(180deg, var(--sky) 0%, var(--facade) 18%, var(--facade) 58%, var(--cladding) 62%, var(--cladding) 85%, var(--street) 100%);
  }
  .details {
    position: relative;
    width: 689px;
    height: 851px;
    background: var(--navy);
    color: var(--ink);
    text-align: center;
  }
  .corner-flourish {
    position: absolute;
    width: 158px;
    height: 158px;
  }
  .corner-flourish.top-right {
    right: 16px; top: 17px;
    background: radial-gradient(circle at 85% 15%, var(--gold-soft), transparent 70%);
  }
  .corner-flourish.bottom-left {
    left: 11px; bottom: 17px;
    background: radial-gradient(circle at 15% 85%, var(--gold-soft), transparent 70%);
  }
  .brand {
    position: absolute;
    left: 0; right: 0; top: 42px;
    display: flex;
    flex-direction: column;
    align-items: center;
    color: var(--gold);
    font-family: "Lora", serif;
    font-weight: 400;
  }
  .brand-circle {
    width: 54px; height: 54px;
    border: 2px solid var(--gold);
    border-radius: 50%;
  }
  .brand-name {
    margin-top: 6px;
    font-size: 19px;
    letter-spacing: 0.5px;
    line-height: 1.1;
  }
  .brand-sub {
    font-size: 8px;
    letter-spacing: 6px;
    padding-left: 6px;
  }
  .headline {
    position: absolute;
    left: 0; right: 0; top: 161px;
    font-family: "Lora", serif;
    font-style: italic;
    font-size: 24px;
    line-height: 30px;
    color: var(--ink);
  }
  .message {
    position: absolute;
    left: 104px; width: 481px; top: 294px;
    font-family: "Fira Sans", sans-serif;
    font-weight: 300;
    font-size: 17px;
    line-height: 22.8px;
    color: var(--ink);
  }
  .message p + p { margin-top: 22.8px; }
  .email-icon { display: inline-block; vertical-align: -2px; margin-right: 4px; }
  .event-facts {
    position: absolute;
    left: 95px; width: 500px; top: 688px;
    font-family: "Libre Baskerville", serif;
    font-weight: 700;
    font-size: 17.5px;
    line-height: 22.8px;
    color: var(--white);
  }
</style>
</head>
<body>
<main class="invite">
  <div class="building-photo" role="img" aria-label="Photo of the four-storey Halvorsen building with dark siding, wood-clad ground floor and a grey convertible parked in front"></div>

  <section class="details">
    <div class="corner-flourish top-right" role="img" aria-label="Gold ornamental corner flourish"></div>
    <div class="corner-flourish bottom-left" role="img" aria-label="Gold ornamental corner flourish"></div>

    <div class="brand">
      <span class="brand-circle"></span>
      <span class="brand-name">LARCHMONT</span>
      <span class="brand-sub">REALTY</span>
    </div>

    <h1 class="headline">
      You’re Cordially Invited<br>
      To a Sunset Celebration Honoring the<br>
      Launch of The Halvorsen
    </h1>

    <div class="message">
      <p>Please join us for an elegant evening of connection and celebration as we unveil The Halvorsen Project. Enjoy private tours of Units 3 and 4, along with our breathtaking roof deck offering sweeping views of East Boston at sunset.</p>
      <p>Sip curated selections of beer and wine and savor light seasonal bites as you mingle with colleagues and guests.</p>
      <p>Feel free to bring clients, friends, or family — all are welcome!</p>
      <p>Kindly RSVP to:<br>
        Marisol Penwarden, Larchmont Realty<br>
        <svg class="email-icon" width="17" height="12" viewBox="0 0 17 12" aria-hidden="true"><rect x="0.5" y="0.5" width="16" height="11" rx="1" fill="#dcdcdc" stroke="#9a9a9a"/><path d="M1 1 L8.5 7 L16 1" fill="none" stroke="#9a9a9a"/></svg>Marisol@larchmontexample.com
      </p>
    </div>

    <div class="event-facts">
      Date: Thursday, May 15<br>
      Time: 5:30 PM – 7:30 PM<br>
      Location: The Halvorsen, 214 Quillfield Street, East Boston
    </div>
  </section>
</main>
</body>
</html>
```